Business Card Design

Im looking for a business card that will market/promote myself as in independent/freelancer in the beauty industry. Im looking for something very modern, and clean looking. no specific colors just something that doesnt look cheesy, would like a very professional look

Industry/Entity Type

Business

Contact Information for Business Card

Corinne Baldasso, Hairstylist(Cut, color, blowdry, style, extensions, straightening treatments), makeup artist, red carpet, in-salon, editorial, tv, film, contact is 5073914620 cbstyling@quillmail.net, LA based

```html
<!DOCTYPE html>
<html lang="en">
<head>
<meta charset="utf-8">
<title>Corinne Baldasso – Business Card</title>
<link rel="stylesheet" href="https://fonts.googleapis.com/css2?family=Jost:wght@400;600&display=swap">
<style>
  :root {
    --backdrop: #f0f0f0;
    --card-white: #ffffff;
    --leaf-green: #5fb341;
    --leaf-deep: #2e9a3c;
    --leaf-light: #86c443;
    --bloom-gold: #f7b418;
    --ghost-pattern: #f6f6f6;
    --ink: #1a1a1a;
    --ink-soft: #2b2b2b;
  }
  html, body {
    margin: 0;
    padding: 0;
    width: 1200px;
    height: 1000px;
    overflow: hidden;
    background: var(--backdrop);
  }
  .canvas {
    position: relative;
    width: 1200px;
    height: 1000px;
    background: var(--backdrop);
  }
  .card {
    position: absolute;
    top: 71px;
    width: 489px;
    height: 284px;
    background: var(--card-white);
    overflow: hidden;
  }
  .card--front { left: 90px; }
  .card--back {
    left: 618px;
    box-shadow: 0 1px 4px rgba(0,0,0,0.08);
  }
  .front-artwork {
    position: absolute;
    inset: 0;
    background:
      radial-gradient(ellipse 30% 45% at 8% 30%, var(--bloom-gold) 0%, transparent 70%),
      radial-gradient(ellipse 20% 30% at 62% 80%, var(--bloom-gold) 0%, transparent 70%),
      radial-gradient(ellipse 22% 35% at 25% 55%, var(--card-white) 0%, transparent 80%),
      linear-gradient(100deg, var(--leaf-light) 0%, var(--leaf-deep) 25%, var(--leaf-light) 45%, var(--leaf-green) 70%, var(--leaf-deep) 100%);
    opacity: 0.92;
  }
  .back-artwork {
    position: absolute;
    inset: 0;
    background:
      radial-gradient(ellipse 40% 50% at 30% 50%, var(--ghost-pattern) 0%, transparent 75%),
      radial-gradient(ellipse 40% 50% at 85% 40%, var(--ghost-pattern) 0%, transparent 75%),
      var(--card-white);
  }
  .contact {
    position: absolute;
    left: 57px;
    top: 164px;
    font-family: "Jost", sans-serif;
    font-size: 10px;
    line-height: 13px;
    letter-spacing: 0.6px;
    text-transform: uppercase;
    color: var(--ink-soft);
  }
  .contact__name {
    margin: 0;
    font-weight: 600;
    color: var(--ink);
  }
  .contact__role { margin: 0 0 13px; }
  .contact__line { margin: 0; }
</style>
</head>
<body>
<main class="canvas">
  <section class="card card--front">
    <div class="front-artwork" role="img" aria-label="Symmetric green and golden-yellow stylised leaf and flame pattern filling the card front"></div>
  </section>

  <section class="card card--back">
    <div class="back-artwork" role="img" aria-label="Faint pale grey leaf pattern across the white card back"></div>
    <div class="contact">
      <p class="contact__name">Corinne Baldasso</p>
      <p class="contact__role">Hairstylist • Makeup Artist</p>
      <p class="contact__line">5073914620</p>
      <p class="contact__line">cbstyling@quillmail.net</p>
      <p class="contact__line">LA Based</p>
    </div>
  </section>
</main>
</body>
</html>
```